Join Our Real Estate Team

I would like to purchase a customized version of a design you have previously submitted - https://www.plumvexa.com/design/61937042

I want to create a recruitment AD. I have attached a AD I have created and would like as much of this information on an AD as possible. My main GOAL is to promote $350 Flat Fee (Includes E&O) per Transaction & No Monthly Fees.
I like to use a photo stock as I have in the attachment of various people.
I DON'T want to say "Wanted". Prefer to say something like "STOP Paying High Splits...Keep Most of YOUR hard earned Commissions"
Feel free to use other formats that might fit all the information that I have in my flyer I have uploaded.

Target Market(s)

Realtors

Industry/Entity Type

Real Estate

Font styles to use
Serif

Colors
0094D4
00A9DD
6FCCEA
C7EBF8
E9F6FB

Requirements
Must have
• See uploaded flyer to get must haves
Nice to have
• See uploaded flyer to get ideas
Should not have
• Do not want it to say "wanted"

```html
<!DOCTYPE html>
<html lang="en">
<head>
<meta charset="utf-8">
<title>Join Our Team – Coastal Palm Realty Group</title>
<link rel="stylesheet" href="https://fonts.googleapis.com/css2?family=Montserrat:wght@400;500;700;800;900&display=swap">
<style>
  :root {
    --blue: #00a9dd;
    --blue-soft: #4fb8e6;
    --blue-light: #6fccea;
    --blue-pale: #c7ebf8;
    --ink: #1d1d1f;
    --text: #2e2e33;
    --grey-panel: #d3d3d5;
    --grey-stripe: #c9c9cc;
    --band: #2b2a30;
    --white: #ffffff;
  }
  * { box-sizing: border-box; margin: 0; padding: 0; }
  html, body { width: 846px; height: 1200px; overflow: hidden; background: var(--white); }
  .flyer {
    position: relative; width: 846px; height: 1200px; overflow: hidden;
    background: var(--white); font-family: "Montserrat", Arial, sans-serif; color: var(--text);
  }
  .abs { position: absolute; }
  .hero-photo {
    left: 300px; top: 0; width: 546px; height: 572px;
    background: linear-gradient(135deg, #eef1f3 0%, #d9dee3 45%, #5b6470 70%, #e9e4de 100%);
  }
  .hero-shapes { left: 0; top: 0; width: 846px; height: 600px; }
  .brand { left: 40px; top: 70px; display: flex; align-items: center; gap: 12px; }
  .brand-mark { width: 20px; height: 20px; background: var(--blue-soft); flex: none; }
  .brand-name { font-weight: 700; color: var(--text); font-size: 21px; line-height: 26px; }
  .services {
    left: 36px; top: 164px; width: 440px; font-weight: 500;
    font-size: 25px; line-height: 36px; color: var(--text);
  }
  .services .lead { padding-left: 4px; }
  .headline {
    left: 34px; top: 300px; font-weight: 900;
    font-size: 80px; line-height: 83px; color: var(--white); letter-spacing: 2px;
  }
  .fee-box {
    left: 38px; top: 588px; width: 312px; height: 148px; border: 2px solid var(--blue-soft);
    text-align: center; background: var(--white);
  }
  .fee-amount { font-weight: 900; font-size: 46px; line-height: 50px; color: var(--ink); margin-top: 6px; }
  .fee-label { font-weight: 900; font-size: 47px; line-height: 48px; color: var(--blue); letter-spacing: 1px; }
  .fee-note { font-weight: 500; font-size: 27px; line-height: 34px; color: var(--blue); letter-spacing: 1px; }
  .perks {
    left: 66px; top: 736px; width: 262px; height: 320px; background: var(--grey-panel);
    font-size: 22px; line-height: 24px; text-align: center; color: var(--ink); padding-top: 14px;
  }
  .perks p + p { margin-top: 26px; }
  .example { left: 352px; top: 622px; width: 466px; text-align: center; font-size: 22px; line-height: 26px; color: var(--ink); }
  .frustration { left: 382px; top: 748px; width: 440px; text-align: center; font-size: 22px; line-height: 25px; color: var(--blue); }
  .join { left: 460px; top: 858px; width: 340px; text-align: center; font-weight: 700; font-size: 22px; line-height: 24px; color: var(--ink); }
  .footer-shapes { left: 0; top: 920px; width: 846px; height: 280px; }
  .contact-left { left: 40px; top: 1072px; color: var(--white); font-size: 21px; line-height: 40px; }
  .contact-left .highlight { color: var(--blue-light); }
  .contact-right { left: 480px; top: 1008px; width: 340px; text-align: center; color: var(--white); }
  .call { font-size: 40px; line-height: 48px; font-weight: 500; }
  .call strong { font-weight: 800; }
  .phone { font-size: 45px; line-height: 56px; font-weight: 800; letter-spacing: 1px; }
  .broker { font-size: 21px; line-height: 40px; letter-spacing: 1px; }
</style>
</head>
<body>
<main class="flyer">
  <div class="abs hero-photo" role="img" aria-label="Stock photo of a smiling real estate agent in a suit shaking hands with a client across an office desk"></div>

  <svg class="abs hero-shapes" viewBox="0 0 846 600" aria-hidden="true">
    <polygon points="0,0 330,0 258,150 0,150" fill="var(--white)"/>
    <polygon points="0,150 500,150 700,572 0,572" fill="var(--blue-soft)" opacity=".92"/>
    <polygon points="500,150 560,150 760,572 700,572" fill="var(--blue-pale)" opacity=".55"/>
    <polygon points="330,0 410,0 340,150 258,150" fill="var(--blue-soft)"/>
    <polygon points="430,0 505,0 470,70 395,70" fill="var(--grey-stripe)"/>
    <polygon points="760,485 806,485 766,572 720,572" fill="var(--blue-soft)"/>
    <rect x="0" y="572" width="846" height="28" fill="var(--white)"/>
  </svg>

  <div class="abs brand">
    <div class="brand-mark"></div>
    <div class="brand-name">Coastal Palm<br>Realty Group, LLC</div>
  </div>

  <p class="abs services"><span class="lead">We Are</span><br>Providing Listing, Buying &amp;<br>Property Management Services</p>

  <h1 class="abs headline">LET’S<br>WORK<br>TOGETHER!</h1>

  <div class="abs fee-box">
    <div class="fee-amount">$350*</div>
    <div class="fee-label">FLAT FEE</div>
    <div class="fee-note">*Include E &amp; O</div>
  </div>

  <div class="abs perks">
    <p>PER Transaction<br>No Monthly Fees<br>Timely Payouts</p>
    <p>STOP Paying High<br>Splits Keep Most<br>of YOUR Hard<br>Earned<br>Commissions</p>
  </div>

  <p class="abs example">On A $250.000 Sale w/3% Commission<br>$350*Flat Fee = $7.150<br>Commission Earned&nbsp; w/CPRG</p>

  <p class="abs frustration">Are You FRUSTRATED GIVIN UP<br>20%, 30%, Or Even 50% Of Your<br>Commission???</p>

  <p class="abs join">Join Our Team Start<br>Earning More TODAY !<br>Your&nbsp; FENN<br>&nbsp;&nbsp;omenal Broker</p>

  <svg class="abs footer-shapes" viewBox="0 0 846 280" aria-hidden="true">
    <polygon points="250,130 470,70 470,130" fill="var(--blue-soft)"/>
    <polygon points="0,130 450,130 500,70 846,40 846,280 0,280" fill="var(--band)"/>
    <polygon points="560,58 846,18 846,34 600,66" fill="var(--blue-soft)"/>
  </svg>

  <div class="abs contact-left">
    <p>FENN@CoastPalmRG.com</p>
    <p>www.<span class="highlight">CoastalPalmRealtyGroup</span>.com</p>
  </div>

  <div class="abs contact-right">
    <p class="call"><strong>Call</strong> Us</p>
    <p class="phone">555.204.7816</p>
    <p class="broker">FENN HARLOW</p>
  </div>
</main>
</body>
</html>
```